Pella Acupuncture Business Card Design

I would like a business card design for my acupuncture business which is based from 2 practices in Melbourne, Australia.

The front of the card should include:

*The Logo
* Name - Miranda Tovelisca (B.App.Sc.(TCM), Dip.Rem.Mass.). (I would like the letters after my name in slightly smaller font)
* Mobile number - 0472 318 604
* Web address - www.pellaacupuncture-example.com.au

On the back of the card I would somehow like to fit my 2 clinic addresses in. They are:

The Birchwood Restoration Rooms
842 Fennimore Rd, Camberwell VIC 3124
Ph: 1300 274 518

Quillbrook Integrative & Eastern Herbal Therapy Clinic
31 Marlowby Rd, Malvern East VIC 3145
Ph: (03) 9871 3352

If there is space, I'd also like to add to the back of the card - Next Appointment............................ (or something along those lines).

Thanks and happy designing!

Target Market(s)

Health consumers, and colleagues in the health industry

Industry/Entity Type

Clinic

Contact Information for Business Card

as above in brief

Requirements
Must have
• I've seen some ok designs coming in, however I'd like to avoid the generic look with the added curved line details etc. I don't particularly need extra patterns added to the card. I'd prefer it to look quite clean and simple, and using more earthy colours (I'm not super keen on the lime green that a lot of designs seem to include. I don't mind the full black or white look, (obviously the back side needs to be a lighter colour to allow me to write appointment details on it). I also quite like the idea of the background looking like brown recycled paper (just an idea - that's not 100% necessary).
Nice to have
• I have an idea that I could have the main flower part of the logo printed as metallic.
Should not have
• Generic patterns and too much added detail.

```html
<!DOCTYPE html>
<html lang="en">
<head>
<meta charset="utf-8">
<title>Pella Acupuncture – Business Card</title>
<link href="https://fonts.googleapis.com/css2?family=Ubuntu:wght@400;500;700&display=swap" rel="stylesheet">
<style>
  :root {
    --backdrop: #8e8e8e;
    --paper: #eeeeec;
    --paper-shade: #e2e2e0;
    --ink: #262626;
    --charcoal: #232323;
    --earth: #8a6a44;
    --white: #ffffff;
    --muted: #eadfcf;
    --label: #777777;
    --rule: #555555;
  }
  * { box-sizing: border-box; margin: 0; padding: 0; }
  html, body { width: 1200px; height: 1000px; overflow: hidden; }
  body {
    background: var(--backdrop);
    font-family: "Ubuntu", sans-serif;
    position: relative;
  }
  .card {
    position: absolute;
    left: 220px;
    width: 760px;
    height: 434px;
    overflow: hidden;
    background: var(--paper);
    box-shadow: 0 6px 18px rgba(0,0,0,0.25);
  }
  .card--front { top: 44px; }
  .card--back { top: 522px; }

  /* Front */
  .front__top {
    position: absolute; inset: 0 0 176px 0;
    background: linear-gradient(180deg, var(--paper) 0%, var(--paper-shade) 100%);
  }
  .front__band {
    position: absolute; left: 0; right: 0; bottom: 0; height: 176px;
    background: var(--charcoal);
  }
  .front__name-tab {
    position: absolute; left: 0; top: 204px; width: 360px; height: 54px;
    background: var(--earth);
    padding: 8px 0 0 40px;
    color: var(--white);
  }
  .front__name { font-size: 21px; font-weight: 700; letter-spacing: 0.3px; line-height: 1.1; }
  .front__quals { font-size: 12px; color: var(--muted); margin-top: 3px; line-height: 1.1; }
  .front__contact {
    position: absolute; left: 40px; top: 282px;
    color: var(--white); font-size: 21px; line-height: 34px;
  }
  .brand-mark {
    position: absolute; left: 450px; top: 32px; width: 290px; height: 290px;
  }
  .brand-mark__name {
    position: absolute; inset: 0;
    display: flex; align-items: center; justify-content: center;
    color: var(--white); font-size: 24px; font-weight: 500;
    text-align: center; line-height: 1.2;
  }

  /* Back */
  .back__panel {
    position: absolute; left: 0; top: 0; bottom: 0; width: 350px;
    background: var(--paper);
  }
  .back__dark {
    position: absolute; left: 350px; right: 0; top: 0; bottom: 0;
    background: var(--charcoal);
    padding: 70px 30px 0 40px;
    color: var(--white);
  }
  .brand-mark--small {
    position: absolute; left: 110px; top: 26px; width: 130px; height: 130px;
  }
  .brand-mark--small .brand-mark__name { font-size: 14px; }
  .appointment {
    position: absolute; left: 60px; top: 180px; width: 260px;
    color: var(--ink);
  }
  .appointment__title { font-size: 22px; font-weight: 700; margin-bottom: 26px; }
  .appointment__field {
    display: flex; align-items: flex-end; gap: 6px;
    font-size: 14px; color: var(--label); margin-bottom: 26px;
  }
  .appointment__line { flex: 1; border-bottom: 2px dotted var(--rule); height: 1px; margin-bottom: 3px; }
  .clinic { margin-bottom: 22px; }
  .clinic__name { font-size: 20px; font-weight: 700; line-height: 1.2; }
  .clinic__detail { font-size: 17px; line-height: 1.45; }
</style>
</head>
<body>

<section class="card card--front" aria-label="Business card front">
  <div class="front__top"></div>
  <div class="front__band"></div>
  <div class="front__name-tab">
    <p class="front__name">Miranda Tovelisca</p>
    <p class="front__quals">(B.App.Sc.(TCM), Dip.Rem.Mass.)</p>
  </div>
  <div class="front__contact">
    <p>m : 0472 318 604</p>
    <p>w : www.pellaacupuncture-example.com.au</p>
  </div>
  <div class="brand-mark">
    <svg width="290" height="290" viewBox="0 0 290 290" aria-hidden="true">
      <circle cx="145" cy="145" r="140" fill="var(--charcoal)" stroke="var(--white)" stroke-width="8"/>
    </svg>
    <p class="brand-mark__name">Pella<br>Acupuncture</p>
  </div>
</section>

<section class="card card--back" aria-label="Business card back">
  <div class="back__panel">
    <div class="brand-mark brand-mark--small">
      <svg width="130" height="130" viewBox="0 0 130 130" aria-hidden="true">
        <circle cx="65" cy="65" r="63" fill="var(--charcoal)"/>
      </svg>
      <p class="brand-mark__name">Pella<br>Acupuncture</p>
    </div>
    <div class="appointment">
      <p class="appointment__title">Next Appointment</p>
      <p class="appointment__field">date : <span class="appointment__line"></span></p>
      <p class="appointment__field">time : <span class="appointment__line"></span></p>
    </div>
  </div>
  <div class="back__dark">
    <div class="clinic">
      <p class="clinic__name">The Birchwood Restoration Rooms</p>
      <p class="clinic__detail">842 Fennimore Rd, Camberwell VIC 3124</p>
      <p class="clinic__detail">Ph: 1300 274 518</p>
    </div>
    <div class="clinic">
      <p class="clinic__name">Quillbrook Integrative &amp; Eastern Herbal Therapy Clinic</p>
      <p class="clinic__detail">31 Marlowby Rd, Malvern East VIC 3145</p>
      <p class="clinic__detail">Ph: (03) 9871 3352</p>
    </div>
  </div>
</section>

</body>
</html>
```